Business card design needed

Card needs to say

Maren Dulworth
Investor - Solutions - Development

My business is in property deals. I would like the words above to be on the card. I have attached a logo for you to copy/recreate.
On the back you could list the following:

Creative property solutions

Thankyou, Maren

Target Market(s)

people wanting to get into the property market, desperate sellers, Mums & Dads wanting to help their kids to purchase a property. People who want to create wealth. People who are stuck and need a solution.

Industry/Entity Type

Business

Contact Information for Business Card

T: 0481 253 407
F: (07) 3584 2719
E: maren47@plx.com.au

Requirements
Must have
• Simple and effective.
Look like I am here to help
Should not have
• Should not look like a realestate agent

```html
<!DOCTYPE html>
<html lang="en">
<head>
<meta charset="utf-8">
<title>Maren Dulworth – Business Cards</title>
<link href="https://fonts.googleapis.com/css2?family=Quicksand:wght@400;500&display=swap" rel="stylesheet">
<style>
  :root {
    --page-bg: #ffffff;
    --card-top: #f5f5f5;
    --card-bottom: #dedede;
    --name-blue: #4f87a3;
    --tagline-grey: #6a6a6a;
    --band-green: #93c55c;
    --rule-blue: #2a8fd0;
    --mark-blue: #2b93d6;
    --contact-white: #ffffff;
  }
  * { margin: 0; padding: 0; box-sizing: border-box; }
  html, body {
    width: 1200px; height: 657px; overflow: hidden;
    background: var(--page-bg);
    font-family: "Quicksand", sans-serif;
  }
  .canvas { position: relative; width: 1200px; height: 657px; }

  .card {
    position: absolute; overflow: hidden;
    background: linear-gradient(to bottom, var(--card-top) 0%, var(--card-top) 30%, var(--card-bottom) 100%);
  }
  .card--landscape { left: 43px; top: 114px; width: 613px; height: 338px; }
  .card--portrait  { left: 766px; top: 42px; width: 353px; height: 581px; }

  .brand {
    position: absolute; left: 0; right: 0;
    display: flex; align-items: center; justify-content: center; gap: 12px;
    color: var(--mark-blue); font-weight: 500; line-height: 1;
  }
  .brand__dot { border-radius: 50%; background: var(--mark-blue); }
  .card--landscape .brand { top: 80px; font-size: 30px; }
  .card--landscape .brand__dot { width: 30px; height: 30px; }
  .card--portrait .brand { top: 110px; font-size: 32px; }
  .card--portrait .brand__dot { width: 32px; height: 32px; }

  .name {
    position: absolute; left: 0; right: 0; text-align: center;
    color: var(--name-blue); font-weight: 500; letter-spacing: 0.3px; line-height: 1;
  }
  .tagline {
    position: absolute; left: 0; right: 0; text-align: center;
    color: var(--tagline-grey); font-weight: 400; line-height: 1;
  }
  .card--landscape .name { top: 206px; font-size: 48px; }
  .card--landscape .tagline { top: 256px; font-size: 22px; }
  .card--portrait .name { top: 302px; font-size: 38px; }
  .card--portrait .tagline { top: 346px; font-size: 19px; }

  .band { position: absolute; left: 0; bottom: 0; width: 100%; }
  .band path.fill { fill: var(--band-green); }
  .band path.rule { fill: none; stroke: var(--rule-blue); stroke-width: 3; }

  .contacts {
    position: absolute; left: 0; right: 0; text-align: center;
    color: var(--contact-white); font-weight: 400; list-style: none;
  }
  .card--landscape .contacts {
    bottom: 7px; font-size: 19px; display: flex; justify-content: center; gap: 7px;
  }
  .card--portrait .contacts { top: 470px; font-size: 21px; line-height: 30px; }
</style>
</head>
<body>
<main class="canvas">

  <section class="card card--landscape" aria-label="Landscape business card">
    <div class="brand"><span class="brand__dot"></span><span>Maren</span></div>
    <h1 class="name">Maren Dulworth</h1>
    <p class="tagline">Investor – Solutions – Development</p>
    <svg class="band" width="613" height="40" viewBox="0 0 613 40" aria-hidden="true">
      <path class="fill" d="M0 12 Q306 -2 613 2 L613 40 L0 40 Z"/>
      <path class="rule" d="M0 11 Q306 -3 613 1"/>
    </svg>
    <ul class="contacts">
      <li>T: 0481 253 407</li>
      <li>F: (07) 3584 2719</li>
      <li>E: maren47@plx.com.au</li>
    </ul>
  </section>

  <section class="card card--portrait" aria-label="Portrait business card">
    <div class="brand"><span class="brand__dot"></span><span>Maren</span></div>
    <h2 class="name">Maren Dulworth</h2>
    <p class="tagline">Investor – Solutions – Development</p>
    <svg class="band" width="353" height="134" viewBox="0 0 353 134" aria-hidden="true">
      <path class="fill" d="M0 12 Q176 -6 353 12 L353 134 L0 134 Z"/>
      <path class="rule" d="M0 11 Q176 -7 353 11"/>
    </svg>
    <ul class="contacts">
      <li>T: 0481 253 407</li>
      <li>F: (07) 3584 2719</li>
      <li>E: maren47@plx.com.au</li>
    </ul>
  </section>

</main>
</body>
</html>
```